****Business Card Design for Cormwell Development. Design based around attached logo/company name

I’m looking for business card design for my company Cormwell Development Group,LLC. Design should be professional, sharp and minimal. Outside of the attached logos, greyscale colors for remainder of cards. My thoughts are two-sided card with attached logo on one side and my info on the other but open to one-sided as well with right design.
Target Market(s)
Real estate professionals including banks, private investors, property owners, developers, commercial tenants like Brewlantic, Granvey or Tamsett’s.
Industry/Entity Type
Commercial real estate development and investments.
Contact Information for Business Card
Name, title, email, phone #’s, web address and physical address
Font styles to use
Other font styles liked:
- Helvetica, Garamond, etc
Colors
Designer to choose only greyscale colors for use in the design.
Requirements
Must have
- Attached logo first or second options.
Nice to have
- Two sided card with logo on one side. Attached Logo/company name can be laid out any way that flows as long as it’s legible.name
Should not have
- No loud colors. ***Please do not include logo, I have removed the company design with a logo image.

```html
<!DOCTYPE html>
<html lang="en">
<head>
<meta charset="UTF-8">
<title>Cormwell Development Group, LLC — Business Cards</title>
<link rel="stylesheet" href="https://fonts.googleapis.com/css2?family=Cormorant+Garamond:wght@500&family=Arimo:wght@400&display=swap">
<style>
  :root {
    --stage: #d6d7db;
    --card: #5f6678;
    --paper: #ffffff;
    --company: #eef0f3;
    --ink-muted: #6b7080;
    --contact: #f4f5f7;
    --shadow: rgba(30, 34, 44, 0.35);
  }
  * { margin: 0; padding: 0; box-sizing: border-box; }
  html, body { width: 804px; height: 1200px; overflow: hidden; }
  body { background: var(--stage); position: relative; }

  .card {
    position: absolute;
    left: 102px;
    width: 600px;
    height: 343px;
    background: var(--card);
    box-shadow: 10px 14px 22px var(--shadow);
    overflow: hidden;
  }
  .card--front { top: 170px; }
  .card--back { top: 660px; }

  .company-name {
    position: absolute;
    left: 0; right: 0;
    text-align: center;
    font-family: "Cormorant Garamond", serif;
    font-weight: 500;
    color: var(--company);
    line-height: 1.1;
    white-space: nowrap;
  }
  .card--front .company-name { top: 150px; font-size: 34px; }
  .card--back .company-name { top: 58px; font-size: 30px; }

  .name-band {
    position: absolute;
    left: 0; top: 172px;
    width: 264px; height: 100px;
    background: var(--paper);
    padding: 28px 0 0 58px;
  }
  .name-band__name {
    font-family: "Cormorant Garamond", serif;
    font-weight: 500;
    font-size: 26px;
    color: var(--ink-muted);
    line-height: 1;
  }
  .name-band__title {
    font-family: "Arimo", sans-serif;
    font-size: 10px;
    color: var(--ink-muted);
    letter-spacing: 0.08em;
    margin-top: 6px;
  }

  .contact-list {
    position: absolute;
    left: 276px; top: 174px;
    list-style: none;
  }
  .contact-list__item {
    display: flex;
    align-items: flex-start;
    gap: 10px;
    font-family: "Arimo", sans-serif;
    font-size: 13px;
    line-height: 15px;
    color: var(--contact);
    margin-bottom: 7px;
  }
  .contact-list__icon {
    flex: 0 0 16px;
    width: 16px; height: 16px;
    background: var(--paper);
    border-radius: 2px;
  }

  .edge-bar {
    position: absolute;
    left: 574px; top: 172px;
    width: 14px; height: 100px;
    background: var(--paper);
  }
</style>
</head>
<body>
  <section class="card card--front" aria-label="Business card front">
    <div class="company-name">Cormwell Development Group, LLC</div>
  </section>

  <section class="card card--back" aria-label="Business card back">
    <div class="company-name">Cormwell Development Group, LLC</div>

    <div class="name-band">
      <div class="name-band__name">Your Name</div>
      <div class="name-band__title">DESIGNATION</div>
    </div>

    <ul class="contact-list">
      <li class="contact-list__item">
        <svg class="contact-list__icon" viewBox="0 0 16 16" aria-hidden="true">
          <path d="M4.5 3.5h2l1 2.5-1.3 1a6 6 0 0 0 2.8 2.8l1-1.3 2.5 1v2a1 1 0 0 1-1 1A8.5 8.5 0 0 1 3.5 4.5a1 1 0 0 1 1-1z" fill="var(--card)"/>
        </svg>
        <span>+0000 536 3824</span>
      </li>
      <li class="contact-list__item">
        <svg class="contact-list__icon" viewBox="0 0 16 16" aria-hidden="true">
          <rect x="3" y="4.5" width="10" height="7" fill="none" stroke="var(--card)" stroke-width="1.2"/>
          <path d="M3 4.5l5 4 5-4" fill="none" stroke="var(--card)" stroke-width="1.2"/>
        </svg>
        <span>info@companyname.com</span>
      </li>
      <li class="contact-list__item">
        <svg class="contact-list__icon" viewBox="0 0 16 16" aria-hidden="true">
          <circle cx="8" cy="8" r="4.8" fill="none" stroke="var(--card)" stroke-width="1.1"/>
          <ellipse cx="8" cy="8" rx="2" ry="4.8" fill="none" stroke="var(--card)" stroke-width="1"/>
          <path d="M3.2 8h9.6" stroke="var(--card)" stroke-width="1"/>
        </svg>
        <span>www.companyname.com</span>
      </li>
      <li class="contact-list__item">
        <svg class="contact-list__icon" viewBox="0 0 16 16" aria-hidden="true">
          <path d="M8 13.5s-4-4.2-4-7a4 4 0 0 1 8 0c0 2.8-4 7-4 7z" fill="var(--card)"/>
          <circle cx="8" cy="6.4" r="1.5" fill="var(--paper)"/>
        </svg>
        <span>Your City Address, Street Location<br>NY City, USA</span>
      </li>
    </ul>

    <div class="edge-bar"></div>
  </section>
</body>
</html>
```